Children's Educational Software - Login Screens

We need graphics for some basic login pages. The main requirements are a background image, buttons and background overlay (box for login fields and app icons). Must utilize responsive design for various resolutions and devices. The mock-up file provides an example of the direction we are wanting to go. The app page will require a version of the background that extends down using a solid colour. One idea would be to add some flowers, bees, etc. to help add some life to the bottom half. I like the idea of clouds and grass, but am open to anything.

Target Market(s)

Elementary teachers and young children

Coding

Coded - Design and coding required

Number of Pages Required

2 page

Font styles to use
Sans Serif

Requirements
Must have
• Responsive design for various resolutions and devices
Nice to have
• clouds, grass, new app icons if current icons don't fit with new design

```html
<!DOCTYPE html>
<html lang="en">
<head>
<meta charset="utf-8">
<title>Program Selection</title>
<link rel="stylesheet" href="https://fonts.googleapis.com/css2?family=Montserrat:wght@400;500;600;700;800&family=Dancing+Script:wght@600&display=swap">
<style>
  :root {
    --navy: #1e3a78;
    --ink: #1d2d55;
    --rule: #c9d3df;
    --sky-top: #ffffff;
    --sky-bottom: #e2f1fb;
    --accent: #35b6f0;
    --blue: #4d8ae6;
    --blue-dark: #3a74d6;
    --red: #e64a5d;
    --red-dark: #d7384c;
    --yellow: #f8b93b;
    --yellow-dark: #f2a622;
    --green: #3ac79c;
    --green-dark: #27b487;
    --pink: #e77dbf;
    --pink-dark: #db66ae;
    --grass: #c9e58a;
    --grass-deep: #a9d35f;
  }
  * { box-sizing: border-box; margin: 0; padding: 0; }
  html, body { width: 1200px; height: 2416px; overflow: hidden; }
  body {
    position: relative;
    font-family: "Montserrat", sans-serif;
    color: var(--ink);
    background: linear-gradient(180deg, var(--sky-top) 0%, var(--sky-top) 8%, var(--sky-bottom) 70%, #d6edfb 100%);
  }

  /* Header */
  .site-header {
    position: absolute; left: 0; top: 0; width: 1200px; height: 110px;
    background: var(--navy);
    box-shadow: 0 4px 14px rgba(20, 40, 90, 0.18);
  }
  .brand {
    position: absolute; left: 68px; top: 30px; height: 50px;
    display: flex; align-items: center; gap: 16px;
  }
  .brand-mark { width: 50px; height: 50px; background: var(--accent); border-radius: 8px; }
  .brand-title { font-size: 18px; font-weight: 700; color: #fff; }
  .brand-title span { color: var(--accent); }
  .contact {
    position: absolute; right: 60px; top: 32px; height: 46px;
    display: flex; align-items: center; gap: 24px;
  }
  .contact-phone { font-size: 17px; font-weight: 500; color: #d9e2f2; }
  .contact-mail {
    width: 46px; height: 46px; border-radius: 50%; background: #fff;
    display: flex; align-items: center; justify-content: center;
  }

  /* Sections */
  .program-section { position: absolute; left: 142px; width: 916px; }
  .section-title {
    font-size: 35px; font-weight: 600; color: var(--navy); letter-spacing: 0.2px;
    padding-bottom: 10px; border-bottom: 1.5px solid var(--rule);
  }
  .reading { top: 190px; }
  .math { top: 1173px; }

  .app-grid {
    position: absolute; left: -24px; width: 952px;
    display: grid; grid-template-columns: repeat(4, 238px); grid-auto-rows: 213px;
  }
  .reading .app-grid { top: 106px; }
  .math .app-grid { top: 99px; }

  .app { display: flex; flex-direction: column; align-items: center; }
  .app-icon { position: relative; width: 120px; height: 120px; }
  .app-icon::before {
    content: ""; position: absolute; left: 10px; top: 6px; width: 120px; height: 120px;
    border-radius: 48% 52% 50% 50%; background: #fff;
    box-shadow: 0 6px 14px rgba(40, 70, 120, 0.08);
  }
  .app-blob {
    position: absolute; inset: 0; border-radius: 50% 48% 52% 50%;
    background: var(--c);
    display: flex; align-items: center; justify-content: center;
    font-size: 40px; font-weight: 800; color: #fff; letter-spacing: 0.5px;
  }
  .app-badge {
    position: absolute; right: 2px; top: -6px; width: 32px; height: 32px; border-radius: 50%;
    background: var(--cd); border: 3px solid rgba(255,255,255,0.55);
    display: flex; align-items: center; justify-content: center;
    font-size: 15px; font-weight: 700; color: #fff;
  }
  .app-badge.plain { background: var(--c); filter: brightness(1.06); }
  .app-dot {
    position: absolute; left: 76px; top: -20px; width: 8px; height: 8px; border-radius: 50%;
    background: var(--cd);
  }
  .app-name {
    margin-top: 24px; font-size: 12.5px; font-weight: 600; color: var(--ink);
    text-align: center; line-height: 1.4; letter-spacing: 0.3px; white-space: nowrap;
  }

  .blue   { --c: var(--blue);   --cd: var(--blue-dark); }
  .red    { --c: var(--red);    --cd: var(--red-dark); }
  .yellow { --c: var(--yellow); --cd: var(--yellow-dark); }
  .green  { --c: var(--green);  --cd: var(--green-dark); }
  .pink   { --c: var(--pink);   --cd: var(--pink-dark); }

  /* Meadow scene */
  .meadow {
    position: absolute; left: 0; top: 1960px; width: 1200px; height: 386px;
    background: linear-gradient(180deg, rgba(214,237,251,0) 0%, #d5ecf7 55%, var(--grass) 82%, var(--grass-deep) 100%);
  }

  /* Footer */
  .site-footer {
    position: absolute; left: 0; top: 2346px; width: 1200px; height: 70px;
    background: var(--navy);
  }
  .copyright { position: absolute; left: 68px; top: 28px; font-size: 11px; color: #c5d0e4; }
  .trust {
    position: absolute; left: 618px; top: 23px; font-size: 18px; font-weight: 500; color: #c9d4e8;
  }
  .trust strong { color: var(--accent); font-weight: 700; }
  .subscribe {
    position: absolute; left: 971px; top: 14px; width: 157px; height: 42px;
    border: 1.5px solid #c9d4e8; border-radius: 21px;
    display: flex; align-items: center; justify-content: center; gap: 10px;
    font-family: "Dancing Script", cursive; font-size: 19px; color: #fff;
  }
</style>
</head>
<body>

<header class="site-header">
  <div class="brand">
    <span class="brand-mark"></span>
    <span class="brand-title">Program <span>Selection</span></span>
  </div>
  <div class="contact">
    <span class="contact-phone">Call. 1 800 555 0142</span>
    <span class="contact-mail">
      <svg width="22" height="16" viewBox="0 0 22 16" aria-hidden="true">
        <rect x="1" y="1" width="20" height="14" rx="2" fill="none" stroke="#35b6f0" stroke-width="2"/>
        <path d="M2 2 L11 9 L20 2" fill="none" stroke="#35b6f0" stroke-width="2"/>
      </svg>
    </span>
  </div>
</header>

<section class="program-section reading">
  <h2 class="section-title">Reading &amp; Language</h2>
  <div class="app-grid">
    <div class="app blue"><div class="app-icon"><span class="app-blob">CR</span><span class="app-dot"></span><span class="app-badge">K</span></div><p class="app-name">Core Reading<br>Kindergarten</p></div>
    <div class="app blue"><div class="app-icon"><span class="app-blob">CR</span><span class="app-dot"></span><span class="app-badge">1</span></div><p class="app-name">Core Reading</p></div>
    <div class="app blue"><div class="app-icon"><span class="app-blob">CR</span><span class="app-dot"></span><span class="app-badge">2</span></div><p class="app-name">Core Reading</p></div>
    <div class="app blue"><div class="app-icon"><span class="app-blob">CR</span><span class="app-dot"></span><span class="app-badge">3</span></div><p class="app-name">Core Reading</p></div>

    <div class="app red"><div class="app-icon"><span class="app-blob">RS</span><span class="app-dot"></span><span class="app-badge plain"></span></div><p class="app-name">Reading Sparks</p></div>
    <div class="app red"><div class="app-icon"><span class="app-blob">PS</span><span class="app-dot"></span><span class="app-badge plain"></span></div><p class="app-name">Phonics Starter</p></div>
    <div class="app yellow"><div class="app-icon"><span class="app-blob">SP</span><span class="app-dot"></span><span class="app-badge plain"></span></div><p class="app-name">Sound Play</p></div>
    <div class="app yellow"><div class="app-icon"><span class="app-blob">SP</span><span class="app-dot"></span><span class="app-badge">2</span></div><p class="app-name">Sound Play 2</p></div>

    <div class="app yellow"><div class="app-icon"><span class="app-blob">SW</span><span class="app-dot"></span><span class="app-badge plain"></span></div><p class="app-name">Star Words</p></div>
    <div class="app yellow"><div class="app-icon"><span class="app-blob">SW</span><span class="app-dot"></span><span class="app-badge">2</span></div><p class="app-name">Star Words 2</p></div>
    <div class="app green"><div class="app-icon"><span class="app-blob">FS</span><span class="app-dot"></span><span class="app-badge plain"></span></div><p class="app-name">Fun Sounds</p></div>
    <div class="app green"><div class="app-icon"><span class="app-blob">SM</span><span class="app-dot"></span><span class="app-badge">1</span></div><p class="app-name">Spell Mates 1</p></div>

    <div class="app green"><div class="app-icon"><span class="app-blob">SM</span><span class="app-dot"></span><span class="app-badge">2</span></div><p class="app-name">Spell Mates 2</p></div>
    <div class="app green"><div class="app-icon"><span class="app-blob">SM</span><span class="app-dot"></span><span class="app-badge">3</span></div><p class="app-name">Spell Mates 3</p></div>
    <div class="app green"><div class="app-icon"><span class="app-blob">SM</span><span class="app-dot"></span><span class="app-badge">4</span></div><p class="app-name">Spell Mates 4</p></div>
    <div class="app blue"><div class="app-icon"><span class="app-blob">SS</span><span class="app-dot"></span><span class="app-badge plain"></span></div><p class="app-name">Spelling Safari</p></div>
  </div>
</section>

<section class="program-section math">
  <h2 class="section-title">Math</h2>
  <div class="app-grid">
    <div class="app pink"><div class="app-icon"><span class="app-blob">CM</span><span class="app-dot"></span><span class="app-badge">1</span></div><p class="app-name">Count Mates 1</p></div>
    <div class="app pink"><div class="app-icon"><span class="app-blob">CM</span><span class="app-dot"></span><span class="app-badge">2</span></div><p class="app-name">Count Mates 2</p></div>
    <div class="app pink"><div class="app-icon"><span class="app-blob">CM</span><span class="app-dot"></span><span class="app-badge">3</span></div><p class="app-name">Count Mates 3</p></div>
    <div class="app blue"><div class="app-icon"><span class="app-blob">MN</span><span class="app-dot"></span><span class="app-badge plain"></span></div><p class="app-name">Mighty Numbers</p></div>

    <div class="app blue"><div class="app-icon"><span class="app-blob">MN</span><span class="app-dot"></span><span class="app-badge">2</span></div><p class="app-name">Mighty Numbers 2</p></div>
    <div class="app blue"><div class="app-icon"><span class="app-blob">MN</span><span class="app-dot"></span><span class="app-badge">3</span></div><p class="app-name">Mighty Numbers 3</p></div>
    <div class="app green"><div class="app-icon"><span class="app-blob">M</span><span class="app-dot"></span><span class="app-badge plain"></span></div><p class="app-name">Measuring</p></div>
    <div class="app green"><div class="app-icon"><span class="app-blob">MM</span><span class="app-dot"></span><span class="app-badge">1</span></div><p class="app-name">Metric Mates 1</p></div>

    <div class="app green"><div class="app-icon"><span class="app-blob">SM</span><span class="app-dot"></span><span class="app-badge">2</span></div><p class="app-name">Simple<br>Measures 2</p></div>
    <div class="app green"><div class="app-icon"><span class="app-blob">MM</span><span class="app-dot"></span><span class="app-badge">3</span></div><p class="app-name">Metric Mates 3</p></div>
    <div class="app yellow"><div class="app-icon"><span class="app-blob">SP</span><span class="app-dot"></span><span class="app-badge">1</span></div><p class="app-name">Sound Play 1</p></div>
    <div class="app yellow"><div class="app-icon"><span class="app-blob">SP</span><span class="app-dot"></span><span class="app-badge">2</span></div><p class="app-name">Sound Play 2</p></div>
  </div>
</section>

<div class="meadow" role="img" aria-label="Illustrated meadow with green hills, leafy trees, bushes, white flowers and cartoon bees flying across a pale sky"></div>

<footer class="site-footer">
  <p class="copyright">© 2019 Bright Steps Learning.</p>
  <p class="trust">Trusted by over <strong>53,000</strong> teachers</p>
  <a class="subscribe">Subscribe Us
    <svg width="16" height="10" viewBox="0 0 16 10" aria-hidden="true">
      <path d="M1 5 H14 M10 1 L14 5 L10 9" fill="none" stroke="#ffffff" stroke-width="1.5" stroke-linecap="round" stroke-linejoin="round"/>
    </svg>
  </a>
</footer>

</body>
</html>
```